Belcotti Business Cards

Business cards for real estate
Target Market(s)
Real estate
Industry/Entity Type
Real Estate Agent
Font styles to use
Serif
Requirements
Must have
- Photo and logo

```html
<!DOCTYPE html>
<html lang="en">
<head>
<meta charset="UTF-8">
<title>Belcotti Realty Business Card</title>
<link href="https://fonts.googleapis.com/css2?family=Crimson+Text:wght@400;600&display=swap" rel="stylesheet">
<style>
  :root {
    --canvas: #f1f1f1;
    --white: #ffffff;
    --burgundy: #7d1f2c;
    --gold: #c19a58;
    --charcoal: #262729;
    --ink: #1a1a1a;
    --photo-tone: #b9bcc2;
  }
  * { box-sizing: border-box; margin: 0; padding: 0; }
  html, body { width: 1200px; height: 1200px; overflow: hidden; }
  body {
    background: var(--canvas);
    font-family: "Crimson Text", Georgia, serif;
    position: relative;
  }
  .card {
    position: absolute;
    left: 176px; top: 365px;
    width: 847px; height: 470px;
    background: var(--gold);
    overflow: hidden;
  }
  .header-band {
    position: absolute; left: 0; top: 0;
    width: 496px; height: 113px;
    background: var(--white);
  }
  .brand {
    position: absolute; left: 30px; top: 18px;
    display: flex; align-items: center; gap: 22px;
    color: var(--ink);
  }
  .brand-mark {
    width: 70px; height: 70px;
    background: var(--burgundy);
  }
  .brand-name { line-height: 1; font-weight: 400; }
  .brand-name .line-1 { display: block; font-size: 40px; letter-spacing: 1px; }
  .brand-name .line-2 { display: block; font-size: 30px; letter-spacing: 6px; margin-top: 2px; }

  .agent-panel {
    position: absolute; left: 0; top: 120px;
    width: 422px; height: 350px;
    background: var(--burgundy);
    border-top-right-radius: 60px;
    color: var(--white);
  }
  .agent-name {
    position: absolute; left: 34px; top: 36px;
    font-size: 62px; line-height: 1; font-weight: 400;
  }
  .agent-tagline {
    position: absolute; left: 34px; top: 94px;
    font-size: 18px; color: var(--gold);
  }
  .agent-contact {
    position: absolute; left: 34px; top: 122px;
    list-style: none; font-size: 20px; line-height: 27px;
  }
  .office-name {
    position: absolute; left: 24px; top: 230px;
    font-size: 19px; letter-spacing: 0.3px;
  }
  .office-contact {
    position: absolute; left: 24px; top: 257px;
    list-style: none; font-size: 10px; line-height: 13px; font-weight: 600;
  }

  .accent-band {
    position: absolute; left: 484px; top: 121px;
    width: 363px; height: 162px;
    background: var(--burgundy);
  }
  .portrait-panel {
    position: absolute; left: 496px; top: 0;
    width: 339px; height: 466px;
    background: var(--charcoal);
    border-bottom-left-radius: 42px;
    border-bottom-right-radius: 42px;
    color: var(--white);
  }
  .portrait-frame {
    position: absolute; left: 62px; top: 53px;
    width: 228px; height: 230px;
    background: var(--gold);
    padding: 7px;
  }
  .portrait-photo {
    width: 100%; height: 100%;
    background: linear-gradient(180deg, #eceef0 0%, var(--photo-tone) 55%, #2b2d33 100%);
  }
  .portrait-name {
    position: absolute; left: 50px; top: 291px;
    font-size: 60px; line-height: 1; font-weight: 400;
  }
  .portrait-tagline {
    position: absolute; left: 53px; top: 347px;
    font-size: 17px; color: var(--gold);
  }
  .portrait-brand {
    position: absolute; left: 0; right: 0; top: 398px;
    text-align: center; font-size: 20px; letter-spacing: 2px;
    color: var(--white);
  }
</style>
</head>
<body>
  <div class="card">
    <div class="header-band">
      <div class="brand">
        <span class="brand-mark"></span>
        <span class="brand-name"><span class="line-1">BELCOTTI</span><span class="line-2">REALTY</span></span>
      </div>
    </div>

    <div class="agent-panel">
      <h1 class="agent-name">Castellano</h1>
      <p class="agent-tagline">Premier Network</p>
      <ul class="agent-contact">
        <li>Street location, NY City, USA</li>
        <li>Cell :+1 555 010 2233</li>
        <li>agent@belcottimail.com</li>
      </ul>
      <p class="office-name">BELCOTTI REALTY</p>
      <ul class="office-contact">
        <li>Street location, NY City, USA</li>
        <li>Office :&nbsp; +1 555 0190</li>
        <li>office@belcotti.com</li>
        <li>www.belcottirealty.com</li>
      </ul>
    </div>

    <div class="accent-band"></div>

    <div class="portrait-panel">
      <div class="portrait-frame">
        <div class="portrait-photo" role="img" aria-label="Portrait photo of the agent in a dark suit and blue tie"></div>
      </div>
      <p class="portrait-name">Castellano</p>
      <p class="portrait-tagline">Premier Network</p>
      <p class="portrait-brand">BELCOTTI</p>
    </div>
  </div>
</body>
</html>
```